Ski and Snowboard Instructor Business card

An eye catching business card capturing the essence of the sport and the mountain with a professional finish and easily readable contact information.

Notes on uploaded files:
I must have the KORVE (Northern Guild of Alpine Coaching Standards) Logo featured on the design (I designed it on the front but you can move if you think it would look better else where). The front of the card as you will see is a picture of a mountain top, if you can find a real image of this with a clear blue sky and snow that would be great -even better if it was from New Zealand as that is where I will be using the card!!! but also I am open to creative ones - logo style, 2D mountain outline etc.
As for the back something clean and simple, I originally designed it as matt black background with stylised writing for my name and a contrasting colour for the other writing. Possibly add the tag line 'certified snowsports instructor' I didn't just because of spacing etc but I'm keen to see what you guys come up with.

Writing on the back
Jamie Whitcombe
SKI - SNOWBOARD
jamiewhitcombe2008@frostmail.example
NZ: 02107481639
UK: (+44) 07835519402
Hope this helps
Happy designing!

Industry/Entity Type

Business

Contact Information for Business Card

See description

Requirements
Must have
• KORVE (Northern guild of Alpine Coaching Standards) logo. It is a trademarked logo so please no alterations in shape or colour.
Nice to have
• Real Images of mountains, snow etc

```html
<!DOCTYPE html>
<html lang="en">
<head>
<meta charset="utf-8">
<title>Jamie Whitcombe – Snowsports Instructor Business Card</title>
<link href="https://fonts.googleapis.com/css2?family=Kaushan+Script&family=Open+Sans:wght@300;400;600&family=Roboto+Condensed:wght@700&display=swap" rel="stylesheet">
<style>
  :root {
    --page-bg: #e9e7e3;
    --card-black: #0d0d0d;
    --sky-top: #1f5fb8;
    --sky-mid: #3b86d6;
    --snow: #e8eef5;
    --rock: #5a6a80;
    --name-blue: #1f86d8;
    --accent-red: #e0352b;
    --contact-grey: #c9c9c9;
    --white: #ffffff;
  }
  * { margin: 0; padding: 0; box-sizing: border-box; }
  html, body {
    width: 1200px;
    height: 595px;
    overflow: hidden;
    background: var(--page-bg);
  }
  .sheet {
    width: 1200px;
    height: 595px;
    display: flex;
    align-items: center;
    justify-content: center;
    gap: 60px;
  }
  .card {
    position: relative;
    width: 510px;
    height: 292px;
    border-radius: 4px;
    overflow: hidden;
    box-shadow: 0 8px 22px rgba(0,0,0,0.25);
  }

  /* Front */
  .card-front .mountain-photo {
    position: absolute;
    inset: 0;
    background:
      radial-gradient(ellipse 70% 55% at 55% 75%, var(--snow) 0%, rgba(232,238,245,0.85) 40%, rgba(90,106,128,0.6) 70%, transparent 85%),
      linear-gradient(160deg, var(--sky-top) 0%, var(--sky-mid) 45%, #8fb4dc 100%);
  }
  .brand-mark {
    position: absolute;
    top: 22px;
    right: 26px;
    display: flex;
    align-items: center;
    gap: 8px;
    font-family: 'Open Sans', sans-serif;
    font-weight: 600;
    font-size: 28px;
    letter-spacing: 2px;
    color: var(--white);
  }
  .brand-mark .brand-square {
    width: 22px;
    height: 22px;
    background: var(--white);
  }
  .card-front .holder-name {
    position: absolute;
    left: 26px;
    bottom: 26px;
    font-family: 'Kaushan Script', cursive;
    font-size: 34px;
    line-height: 1.05;
    color: var(--white);
  }
  .card-front .holder-name span { display: block; }
  .card-front .holder-name .surname { padding-left: 28px; }

  /* Back */
  .card-back {
    background: var(--card-black);
    padding: 34px 40px;
    text-align: center;
  }
  .card-back .holder-name {
    font-family: 'Kaushan Script', cursive;
    font-size: 44px;
    color: var(--name-blue);
    line-height: 1.1;
  }
  .card-back .tagline {
    font-family: 'Open Sans', sans-serif;
    font-weight: 400;
    font-size: 15px;
    color: var(--accent-red);
    margin-top: 4px;
  }
  .card-back .disciplines {
    font-family: 'Roboto Condensed', sans-serif;
    font-weight: 700;
    font-size: 28px;
    color: var(--accent-red);
    margin-top: 14px;
    letter-spacing: 0.5px;
  }
  .card-back .contact-list {
    list-style: none;
    margin-top: 14px;
    font-family: 'Open Sans', sans-serif;
    font-weight: 300;
    font-size: 14px;
    line-height: 1.6;
    color: var(--contact-grey);
  }
</style>
</head>
<body>
  <main class="sheet">
    <section class="card card-front" aria-label="Business card front">
      <div class="mountain-photo" role="img" aria-label="Photograph of a snow-covered mountain summit under a clear blue sky"></div>
      <div class="brand-mark"><span class="brand-square"></span>KORVE</div>
      <h1 class="holder-name"><span>Jamie</span><span class="surname">Whitcombe</span></h1>
    </section>

    <section class="card card-back" aria-label="Business card back">
      <h2 class="holder-name">Jamie Whitcombe</h2>
      <p class="tagline">Certified Snowsports Instructor</p>
      <p class="disciplines">SKI - SNOWBOARD</p>
      <ul class="contact-list">
        <li class="contact-email">jamiewhitcombe2008@frostmail.example</li>
        <li class="contact-phone-nz">NZ: 02107481639</li>
        <li class="contact-phone-uk">UK: (+44) 07835519402</li>
      </ul>
    </section>
  </main>
</body>
</html>
```